TZ BLOOM
transformative skincare
plant-based | clean | anti-aging
The line is for both men and women
-luxurious feeling, plant-based, all natural skincare line
This is a continuation from previous project but maybe with sans serif or serif font instead of cursive for the ML part of Bloom. (Please see logo designs from 2 years ago)
- I think TZ Bloom should be smaller in size than the names of the product so people can more easily read what it says since there are a lot of products in a set.
Also, the day products will have very light cream almost white colored labels with dark green and gold fonts/accents and the night products will have dark green almost black labels with light cream and gold colored font I think.

The products are for both men and women so I don't want the labels looking too feminine? Maybe more simple or a faint leaf design in background.

-about 24 different labels for skincare jars and bottles:
Glycolic Cleanser 4oz and 8oz
Cleansing Oil 4oz and 8oz
Vitamin C Day Serum 1oz and 2oz
Stem Cell C Day Serum 1oz and 2oz
Stem Cell Day Cream 2oz and 4oz
Retinol Night Serum - Lavender 1oz and 2oz
Retinol Night Serum - Neroli 1oz and 2oz
Coconut Charcoal Scrub 2oz and 4oz
Enzyme Night Cream 2oz and 4oz
Eye Renewal Night Serum .5oz
Vitamin C Day Eye Cream .5oz
Honey Lip Balm .5oz
Enzyme Body Lotion - Vanilla Almond 8oz
Enzyme Body Lotion - Mango Lime 8oz
Enzyme Body Lotion - Lavender 8oz

Target Market(s)

ages 40-50 with some 20's and 30's sprinkled in

Industry/Entity Type

Beauty and Skincare

Font styles to use
Serif
Sans Serif
Other font styles liked:
• If you have a more unique but clean or slick font or combo of fonts in mind, please be creative!

Colors
00AB8E
00BBA5
67D7C9
C6EFE9
E9F9F6
FFF300
FFF600
FEFA6F
FFFEC7
FFFEE8

Requirements
Must have
• TZ Bloom should be smaller in size than the names of the product so people can more easily read what it says since there are a lot of products in a set. day products will be light colored labels with dark green and gold fonts/accents and the night products will be on dark green labels with light cream and gold colored font
Nice to have
• Attached are original files of a logo previously designed a couple years ago but not sure I want the script ML anymore? Some sort of leaf design to go with previously made logo but want to see ML in serif or sans serif instead of script. Also attached are simple labels on the products currently and how they look as they're being sold to private clients. Wanting to put them out online for the public this year so need high end, luxurious look and feel but not generic. Thank you!
Should not have
• too busy of a design

```html
<!DOCTYPE html>
<html lang="en">
<head>
<meta charset="utf-8">
<title>TZ Bloom — Vitamin C Day Eye Cream Labels</title>
<link rel="stylesheet" href="https://fonts.googleapis.com/css2?family=Bodoni+Moda:wght@500&family=Montserrat:wght@400;500&family=Raleway:wght@300;400&display=swap">
<style>
  :root {
    --stage: #8e8e8e;
    --forest: #25422e;
    --forest-leaf: #2d5235;
    --cream: #f2efe7;
    --cream-leaf: #dde6cf;
    --gold: #b9924d;
    --gold-light: #f0d58f;
    --gold-deep: #c28a2c;
    --ink-cream: #f3efe4;
  }
  * { margin: 0; padding: 0; box-sizing: border-box; }
  html, body {
    width: 1200px;
    height: 1160px;
    overflow: hidden;
    background: var(--stage);
  }
  .sheet {
    position: relative;
    width: 1200px;
    height: 1160px;
  }
  .label {
    position: absolute;
    left: 146px;
    width: 908px;
    height: 458px;
    overflow: hidden;
    box-shadow: 0 14px 26px rgba(0, 0, 0, 0.35);
  }
  .label--night { top: 104px; background: var(--forest); }
  .label--day { top: 581px; background: var(--cream); }

  .foliage {
    position: absolute;
    border-radius: 46% 54% 40% 60% / 50% 40% 60% 50%;
  }
  .foliage--left { left: 14px; top: 46px; width: 276px; height: 430px; transform: rotate(-8deg); }
  .foliage--right { left: 630px; top: -10px; width: 280px; height: 420px; transform: rotate(14deg); }
  .label--night .foliage { background: radial-gradient(ellipse at center, var(--forest-leaf) 0%, rgba(45, 82, 53, 0) 70%); }
  .label--day .foliage { background: radial-gradient(ellipse at center, var(--cream-leaf) 0%, rgba(221, 230, 207, 0) 70%); }

  .brand {
    position: absolute;
    left: 0;
    width: 100%;
    text-align: center;
  }
  .brand__name {
    top: 80px;
    font-family: "Bodoni Moda", serif;
    font-weight: 500;
    font-size: 50px;
    line-height: 50px;
    letter-spacing: -0.5px;
  }
  .brand__tagline {
    top: 136px;
    font-family: "Montserrat", sans-serif;
    font-weight: 400;
    font-size: 16.5px;
    line-height: 18px;
    letter-spacing: 2.6px;
    color: var(--gold);
  }
  .brand__rule {
    position: absolute;
    left: 341px;
    top: 162px;
    width: 223px;
    height: 1px;
    background: var(--gold);
  }
  .brand__values {
    top: 175px;
    font-family: "Montserrat", sans-serif;
    font-weight: 500;
    font-size: 9.5px;
    line-height: 11px;
    letter-spacing: 1.3px;
  }
  .brand__values-dash {
    display: inline-block;
    width: 27px;
    height: 1px;
    margin: 0 8px 3px;
    vertical-align: middle;
    background: currentColor;
  }
  .product {
    position: absolute;
    left: 0;
    top: 238px;
    width: 100%;
    text-align: center;
    font-family: "Raleway", sans-serif;
    font-weight: 300;
    font-size: 45px;
    line-height: 43px;
  }
  .size {
    position: absolute;
    left: 412px;
    top: 380px;
    width: 83px;
    height: 38px;
    font-family: "Raleway", sans-serif;
    font-weight: 400;
    font-size: 22px;
    line-height: 38px;
    letter-spacing: 1px;
    text-align: center;
  }

  .label--night .brand__name,
  .label--night .brand__values,
  .label--night .product { color: var(--ink-cream); }
  .label--night .size {
    color: var(--forest);
    background: linear-gradient(90deg, var(--gold-light) 0%, #f7ecd0 40%, var(--gold-deep) 75%, #e7c27a 100%);
  }
  .label--day .brand__name,
  .label--day .brand__values { color: var(--forest); }
  .label--day .product { color: var(--gold); }
  .label--day .size { color: var(--ink-cream); background: var(--forest); }
</style>
</head>
<body>
<main class="sheet">

  <section class="label label--night">
    <div class="foliage foliage--left" role="img" aria-label="Faint hand-drawn leafy branch illustration"></div>
    <div class="foliage foliage--right" role="img" aria-label="Faint hand-drawn leafy branch illustration"></div>
    <h1 class="brand brand__name">TZ BLOOM</h1>
    <p class="brand brand__tagline">TRANSFORMATIVE SKINCARE</p>
    <span class="brand__rule"></span>
    <p class="brand brand__values"><span class="brand__values-dash"></span>PLANT-BASED | CLEAN | ANTI-AGING<span class="brand__values-dash"></span></p>
    <h2 class="product">VITAMIN C<br>DAY EYE CREAM</h2>
    <p class="size">5 oz</p>
  </section>

  <section class="label label--day">
    <div class="foliage foliage--left" role="img" aria-label="Faint hand-drawn leafy branch illustration"></div>
    <div class="foliage foliage--right" role="img" aria-label="Faint hand-drawn leafy branch illustration"></div>
    <h1 class="brand brand__name">TZ BLOOM</h1>
    <p class="brand brand__tagline">TRANSFORMATIVE SKINCARE</p>
    <span class="brand__rule"></span>
    <p class="brand brand__values">PLANT-BASED | CLEAN | ANTI-AGING</p>
    <h2 class="product">VITAMIN C<br>DAY EYE CREAM</h2>
    <p class="size">5 oz</p>
  </section>

</main>
</body>
</html>
```